Car transport business

We need a new business card design. Attached is our old card sample. I would just like to adjust the logo colors (blue and red) to be brighter. I changed my name to the brighter red and the word dispatcher to a brighter blue as an example. But you can adjust those colors further. And then perhaps you can use the same colors for the card design but use your imagination.

As a suggestion so the card stands out I would like to add a clip art of car carrier truck. Attached are examples of that as well

```html
<!DOCTYPE html>
<html lang="en">
<head>
<meta charset="utf-8">
<title>Northway Haul – Business Card</title>
<link href="https://fonts.googleapis.com/css2?family=Montserrat:wght@400;500;700&display=swap" rel="stylesheet">
<style>
  :root {
    --page-bg: #dcdcdc;
    --card-white: #ffffff;
    --brand-blue: #165a86;
    --brand-blue-clear: rgba(22, 90, 134, 0);
    --brand-red: #be1e2d;
  }
  * { margin: 0; padding: 0; box-sizing: border-box; }
  html, body {
    width: 1200px; height: 1200px; overflow: hidden;
    background: var(--page-bg);
    font-family: "Montserrat", sans-serif;
  }
  .card {
    position: absolute; left: 200px; width: 759px; height: 433px; overflow: hidden;
  }
  .card-front { top: 108px; background: var(--card-white); }
  .card-back { top: 618px; background: var(--brand-blue); }

  .footer-band {
    position: absolute; left: 0; right: 0; bottom: 0; height: 120px;
    background: linear-gradient(to bottom, var(--brand-blue-clear) 0%, var(--brand-blue) 70%);
  }

  .brand {
    position: absolute; display: flex; align-items: center; gap: 10px;
    font-weight: 700; letter-spacing: 0.5px; text-transform: uppercase; white-space: nowrap;
  }
  .brand-dot { border-radius: 50%; flex: none; }
  .front-brand { left: 62px; top: 196px; color: var(--brand-blue); font-size: 27px; }
  .front-brand .brand-dot { width: 26px; height: 26px; background: var(--brand-blue); }
  .back-brand { left: 0; right: 0; top: 190px; justify-content: center; color: var(--card-white); font-size: 42px; gap: 16px; }
  .back-brand .brand-dot { width: 40px; height: 40px; background: var(--card-white); }

  .divider {
    position: absolute; left: 392px; top: 148px; width: 1.5px; height: 138px; background: var(--brand-red);
  }
  .contact-block { position: absolute; left: 426px; top: 142px; }
  .person-name {
    color: var(--brand-red); font-weight: 500; font-size: 38px; line-height: 1; letter-spacing: 0.5px;
  }
  .person-role {
    color: var(--brand-blue); font-size: 19px; letter-spacing: 0.5px; margin-top: 4px;
  }
  .contact-list { list-style: none; margin-top: 14px; }
  .contact-item {
    display: flex; align-items: center; gap: 7px; color: var(--brand-blue);
    font-size: 19px; line-height: 24.5px; white-space: nowrap;
  }
  .contact-icon { width: 14px; height: 14px; flex: none; }
</style>
</head>
<body>

<section class="card card-front">
  <div class="brand front-brand"><span class="brand-dot"></span>Northway Haul</div>

  <div class="divider"></div>

  <div class="contact-block">
    <h1 class="person-name">LEO MARSH</h1>
    <p class="person-role">DISPATCHER</p>
    <ul class="contact-list">
      <li class="contact-item">
        <svg class="contact-icon" viewBox="0 0 14 14"><path d="M3 1 L5 1 L6 4 L4.5 5.2 Q6 8.5 8.8 9.5 L10 8 L13 9 L13 11 Q12 13 10 13 Q2 11 1 3 Q1 1 3 1Z" fill="none" stroke="var(--brand-red)" stroke-width="1.4"/></svg>
        555-014-2290
      </li>
      <li class="contact-item">
        <svg class="contact-icon" viewBox="0 0 14 14"><rect x="3.5" y="1" width="7" height="4" fill="var(--brand-red)"/><rect x="1" y="5" width="12" height="5.5" rx="1" fill="var(--brand-red)"/><rect x="3.5" y="9" width="7" height="4" fill="var(--brand-red)" stroke="#fff" stroke-width="0.8"/></svg>
        555-014-3381
      </li>
      <li class="contact-item">
        <svg class="contact-icon" viewBox="0 0 14 14"><rect x="1" y="3" width="12" height="8.5" fill="none" stroke="var(--brand-red)" stroke-width="1.3"/><path d="M1 3 L7 8 L13 3" fill="none" stroke="var(--brand-red)" stroke-width="1.3"/></svg>
        northwayhaul@mailbox.com
      </li>
    </ul>
  </div>

  <div class="footer-band" role="img" aria-label="Decorative red and blue swoosh band along the card's lower edge"></div>
</section>

<section class="card card-back">
  <div class="brand back-brand"><span class="brand-dot"></span>Northway Haul</div>
</section>

</body>
</html>
```